HollowPine Ventures Inc. Business Card Design

My business is custom renovations and homes.I would need to have a new business logo created to go along with my company name. The business card should be of a modern style as this is the market I am focused on. I would need my contact information and website posted on the card. I would also like to list a few of the tasks I conduct on the card (such as: Renovations, Additions, Repairs, New Homes, Design, Consultations). On the reverse of the card I currently have just my logo and my motto, "Shaping A Bold Path". However, I am open to completely changing everything as I am starting a new year and would like to excel further. Any new ideas and suggestions are always welcomed. Thank you.

Target Market(s)

Upscale residential and commercial renovations and builds

Industry/Entity Type

Business

Contact Information for Business Card

I would like the design to be able to be laser cut or burnt onto a wooden business card. I will be creating one option of cards for really loyal customers (wooden) and a second option for the everyday customer (paper).

Font styles to use
Other font styles liked:
• Calibri / anything of mordern taste

Colors
f37122
5c5c5c
474747
ffffff

Requirements
Must have
• I would like the colours of my business to be a sharp orange and grey. I believe this will symbolize a modern style. I am open to other suggestions if this is not suitable for the designers tastes. My contact info as follows:
• Will Marsh
• President
• HollowPine Ventures Inc.
• 555-214-3987
• will@hollowpineventures.example
• I would like my website (currently under construction) hollowpineventures.example on the card aswell.
Nice to have
• Along with a modern logo representing HollowPine, I would like something on the card besides the logo and contact information. Perhaps a small background design. I feel it may be nice to have my services listed on the card (in smaller font on the bottom) Renovations, Additions, Repairs, Design, Consultations.
Should not have
• The business card should not have too many different colors. Should not have rounded corners.

```html
<!DOCTYPE html>
<html lang="en">
<head>
<meta charset="utf-8">
<title>HollowPine Ventures Inc. – Business Card</title>
<link rel="stylesheet" href="https://fonts.googleapis.com/css2?family=Open+Sans:wght@400;600&display=swap">
<style>
  :root {
    --orange: #f37122;
    --grey: #474747;
    --grey-mid: #5c5c5c;
    --white: #ffffff;
    --backdrop: #e9e6e3;
  }
  * { margin: 0; padding: 0; box-sizing: border-box; }
  html, body { width: 1200px; height: 800px; overflow: hidden; }
  body {
    background: var(--backdrop);
    font-family: "Open Sans", Arial, sans-serif;
    position: relative;
  }
  .card {
    position: absolute;
    top: 160px;
    width: 270px;
    height: 470px;
    overflow: hidden;
  }
  .card-front { left: 318px; background: var(--grey); }
  .card-back { left: 608px; background: var(--white); }
  .card-art { position: absolute; inset: 0; width: 270px; height: 470px; }

  .front-backdrop {
    position: absolute; inset: 0;
    background: linear-gradient(180deg, var(--orange) 0%, var(--orange) 8%, var(--grey-mid) 32%, var(--grey) 48%, var(--grey) 100%);
  }

  .front-brand {
    position: absolute; top: 168px; left: 0; width: 100%;
    text-align: center; color: var(--white);
  }
  .brand-mark {
    display: block; width: 46px; height: 46px;
    margin: 0 auto 14px; background: var(--orange);
  }
  .brand-name { font-size: 33px; line-height: 1.05; }
  .brand-suffix { font-size: 21px; line-height: 1.3; }
  .services {
    position: absolute; top: 318px; left: 0; width: 100%;
    text-align: center; color: var(--white);
    font-size: 18px; line-height: 27px;
  }
  .services .sep { color: var(--orange); padding: 0 2px; }
  .website {
    position: absolute; top: 443px; left: 0; width: 100%;
    text-align: center; color: var(--white); font-size: 14.5px;
  }

  .back-brand {
    position: absolute; top: 38px; left: 0; width: 100%;
    text-align: center; color: var(--grey);
  }
  .back-brand .brand-mark { width: 44px; height: 44px; margin-bottom: 18px; }
  .back-brand .brand-name { font-size: 32px; }
  .back-brand .brand-suffix { font-size: 21px; }

  .contact {
    position: absolute; top: 262px; left: 0; width: 100%;
    text-align: center; color: var(--white);
  }
  .contact-name {
    display: inline-block; font-size: 25px; line-height: 1.1;
    border-bottom: 2px solid var(--white); padding: 0 2px 1px;
  }
  .contact-title { font-size: 22px; line-height: 1.45; }
  .contact-line { font-size: 13px; line-height: 18px; }
  .contact-line:first-of-type { margin-top: 12px; }
</style>
</head>
<body>

  <section class="card card-front" aria-label="Business card front">
    <div class="front-backdrop" role="img" aria-label="Grey house silhouette with chimney on an orange background"></div>
    <svg class="card-art" viewBox="0 0 270 470" aria-hidden="true">
      <path d="M-10,470 L-10,450 Q135,395 280,450 L280,470 Z"
            fill="var(--orange)" stroke="var(--white)" stroke-width="3"/>
    </svg>

    <div class="front-brand">
      <span class="brand-mark"></span>
      <div class="brand-name">HollowPine</div>
      <div class="brand-suffix">Ventures Inc.</div>
    </div>

    <div class="services">
      <div>Renovations<span class="sep">|</span>Additions</div>
      <div>Repairs<span class="sep">|</span>Design</div>
      <div>Consultations</div>
    </div>

    <div class="website">hollowpineventures.example</div>
  </section>

  <section class="card card-back" aria-label="Business card back">
    <svg class="card-art" viewBox="0 0 270 470" aria-hidden="true">
      <ellipse cx="135" cy="322" rx="215" ry="116" fill="var(--grey)"/>
      <ellipse cx="135" cy="324" rx="215" ry="104" fill="var(--orange)"/>
    </svg>

    <div class="back-brand">
      <span class="brand-mark"></span>
      <div class="brand-name">HollowPine</div>
      <div class="brand-suffix">Ventures Inc.</div>
    </div>

    <div class="contact">
      <div class="contact-name">Will Marsh</div>
      <div class="contact-title">President</div>
      <div class="contact-line">(555)-214-3987</div>
      <div class="contact-line">will@hollowpineventures.example</div>
    </div>
  </section>

</body>
</html>
```